CloudRiver Business Card

I need something that flows with the logo and looks professional but creative. I included the thumbnail file of the photo but will upload the source file once I have it. Colors of business card should flow. I am interested in doing the translucent clear plastic cards as well. My company is called CloudRiver in one word and the contact details are below:

Dale Hollings
555-318-4720
www.CloudRiverTx.example
dhollings_47@mailbox.example
Updates

Too much red. I'd rather focus on the blue and put some silver or grey in there.

New Files uploaded. Like the designs so far and am looking forward to seeing more.

Looking for a whole new direction. Let's forget about the plastic card. Let's focus on the blue more than red. I still haven't seen something that really grabs me.

Industry/Entity Type

Plastic

```html
<!DOCTYPE html>
<html lang="en">
<head>
<meta charset="utf-8">
<title>CloudRiver Business Card</title>
<link rel="stylesheet" href="https://fonts.googleapis.com/css2?family=Exo+2:wght@400;500;600&display=swap">
<style>
  :root{
    --bg:#e9e9ea;
    --card:#ffffff;
    --navy:#174a7c;
    --blue:#1f63a3;
    --blue-mid:#3f86c2;
    --blue-light:#8fbde0;
    --silver:#b9c3cc;
    --silver-light:#dfe5ea;
    --ink:#2b3440;
    --ink-soft:#55606c;
  }
  *{margin:0;padding:0;box-sizing:border-box}
  html,body{width:1200px;height:828px;overflow:hidden;background:var(--bg)}
  body{position:relative;font-family:"Exo 2",sans-serif;color:var(--ink)}
  .card{position:absolute;top:262px;width:530px;height:303px;background:var(--card);
    box-shadow:0 6px 18px rgba(0,0,0,.18);overflow:hidden}
  .card svg.art{position:absolute;inset:0;width:100%;height:100%}
  .card-front{left:40px}
  .card-back{left:630px}
  .brand{position:absolute;display:flex;align-items:center;gap:8px;
    font-weight:600;color:var(--blue);letter-spacing:.5px;white-space:nowrap}
  .brand-dot{width:12px;height:12px;border-radius:50%;background:var(--silver)}
  .card-front .brand{left:68px;top:128px;font-size:44px}
  .card-back .brand{right:28px;bottom:26px;font-size:32px}
  .contact{position:absolute;right:24px;top:24px;text-align:right}
  .contact-name{font-size:19px;font-weight:500;letter-spacing:1.5px;color:var(--blue);text-transform:uppercase}
  .contact-title{font-size:11px;letter-spacing:2px;color:var(--ink-soft);text-transform:uppercase;margin-top:2px}
  .contact-address{font-size:12px;line-height:1.35;margin-top:16px;color:var(--ink)}
  .contact-lines{list-style:none;margin-top:12px;font-size:10px;line-height:1.75;color:var(--ink-soft)}
  .contact-lines li{display:flex;justify-content:flex-end;align-items:center;gap:6px;white-space:nowrap}
  .contact-lines svg{width:10px;height:10px;fill:var(--blue)}
</style>
</head>
<body>

<section class="card card-front" aria-label="Card front">
  <svg class="art" viewBox="0 0 530 303" aria-hidden="true">
    <defs>
      <linearGradient id="front-sweep" x1="0" y1="0" x2="1" y2="0">
        <stop offset="0" stop-color="#dfe5ea" stop-opacity="0"/>
        <stop offset=".5" stop-color="#c7d6e4"/>
        <stop offset="1" stop-color="#fff"/>
      </linearGradient>
    </defs>
    <path d="M250 0 C300 30 340 45 400 40 C460 36 505 55 530 72 V0 Z" fill="url(#front-sweep)" opacity=".8"/>
    <path d="M250 0 C300 26 350 36 405 33 C460 30 505 48 530 68" fill="none" stroke="var(--blue)" stroke-width="4"/>
    <path d="M262 0 C310 20 355 28 410 26 C465 24 505 40 530 56" fill="none" stroke="var(--silver)" stroke-width="2"/>
  </svg>
  <div class="brand"><span class="brand-dot"></span>CloudRiver</div>
</section>

<section class="card card-back" aria-label="Card back">
  <svg class="art" viewBox="0 0 530 303" aria-hidden="true">
    <defs>
      <linearGradient id="blue-panel" x1="0" y1="0" x2="1" y2="1">
        <stop offset="0" stop-color="#3f86c2"/>
        <stop offset="1" stop-color="#174a7c"/>
      </linearGradient>
      <linearGradient id="silver-sweep" x1="0" y1="0" x2="1" y2="0">
        <stop offset="0" stop-color="var(--silver)"/>
        <stop offset="1" stop-color="#fff" stop-opacity="0"/>
      </linearGradient>
    </defs>
    <path d="M245 0 C215 70 300 140 270 210 C255 250 240 280 240 303 H320 C300 250 330 200 340 150 C355 80 300 40 300 0 Z" fill="url(#silver-sweep)" opacity=".8"/>
    <path d="M258 0 C232 70 305 140 276 212 C262 252 248 282 250 303" fill="none" stroke="var(--silver)" stroke-width="9"/>
    <path d="M270 0 C246 70 318 140 290 214 C276 254 262 284 266 303" fill="none" stroke="var(--blue-light)" stroke-width="3"/>
    <path d="M0 0 H245 C215 70 290 140 262 210 C248 250 234 280 236 303 H0 Z" fill="url(#blue-panel)"/>
  </svg>
  <div class="contact">
    <p class="contact-name">Dale Hollings</p>
    <p class="contact-title">Director</p>
    <p class="contact-address">410 Harbor Point Plaza,<br>Suite 12</p>
    <ul class="contact-lines">
      <li>555-318-4720 <svg viewBox="0 0 10 10"><path d="M2 0h2l1 2.5-1.3 1a6 6 0 0 0 2.8 2.8l1-1.3L10 6v2a2 2 0 0 1-2 2A8 8 0 0 1 0 2a2 2 0 0 1 2-2z"/></svg></li>
      <li>555-318-4720 <svg viewBox="0 0 10 10"><rect x="2.5" y="0" width="5" height="10" rx="1"/></svg></li>
      <li>555-318-4720 <svg viewBox="0 0 10 10"><rect x="0" y="3" width="10" height="6" rx="1"/><rect x="2" y="0" width="6" height="3"/></svg></li>
      <li>dhollings_47@mailbox.example <svg viewBox="0 0 10 10"><rect x="0" y="2" width="10" height="6.5" rx="1"/></svg></li>
      <li>www.CloudRiverTx.example <svg viewBox="0 0 10 10"><circle cx="5" cy="5" r="5"/></svg></li>
    </ul>
  </div>
  <div class="brand"><span class="brand-dot"></span>CloudRiver</div>
</section>

</body>
</html>
```